Business cards and stationary design

We just completed the design of our new logo and we need to print new business cards and letterhead for our nonprofit. We are looking for a fresh new design that shows off our new logo. On letterhead, we must have a column on the right or left to include our Board of Directors (up to 45 names) (see attachment)

Industry/Entity Type

Non-Profit

Contact Information for Business Card

Standard business card with name, title, Company name, mailing address phone numbers, email address and website. Tagline on back "Bringing the homeless home"

Font styles to use
Sans Serif

Requirements
Must have
• include pertinent information above
• new logo
• fonts compatible with logo
• should use logo colors only
Nice to have
• tag lines

```html
<!DOCTYPE html>
<html lang="en">
<head>
<meta charset="utf-8">
<title>Harbor Shelter Alliance – Business Card</title>
<link href="https://fonts.googleapis.com/css2?family=Michroma&family=Tinos&display=swap" rel="stylesheet">
<style>
  :root {
    --canvas: #dcdcdc;
    --gold: #f1bf45;
    --gold-light: #f6d36c;
    --bronze: #7d5d18;
    --teal: #137e9c;
    --teal-dark: #0c5f78;
    --accent-red: #e3262e;
    --ink: #4a4a4a;
    --paper: #ffffff;
  }
  * { box-sizing: border-box; margin: 0; padding: 0; }
  html, body { width: 1200px; height: 1200px; overflow: hidden; }
  body { background: var(--canvas); position: relative; font-family: "Tinos", serif; }

  .card {
    position: absolute;
    width: 700px;
    height: 400px;
    box-shadow: 0 12px 30px rgba(0,0,0,.25);
    overflow: hidden;
  }

  /* Front */
  .card-front {
    left: 110px; top: 110px;
    background: linear-gradient(135deg, var(--gold) 0%, var(--gold-light) 100%);
    display: flex; align-items: center; justify-content: center;
  }
  .front-brand { display: flex; flex-direction: column; align-items: center; gap: 14px; }
  .front-brand .brand-row { display: flex; align-items: center; gap: 14px; }
  .front-brand .brand-dot { width: 22px; height: 22px; border-radius: 50%; background: var(--bronze); }
  .front-brand .brand-name {
    font-family: "Michroma", sans-serif; font-size: 26px; letter-spacing: 3px;
    color: var(--bronze); text-transform: uppercase;
  }
  .front-brand .brand-rule { width: 420px; height: 2px; background: var(--bronze); }

  /* Back */
  .card-back { left: 390px; top: 650px; background: var(--paper); }
  .back-bands { position: absolute; inset: 0; }

  .back-brand {
    position: absolute; left: 48px; top: 56px;
    display: flex; align-items: center; gap: 12px;
  }
  .back-brand .brand-dot { width: 20px; height: 20px; border-radius: 50%; background: var(--teal); }
  .back-brand .brand-name {
    font-family: "Michroma", sans-serif; font-size: 20px; letter-spacing: 2px;
    color: var(--teal); text-transform: uppercase;
  }

  .holder { position: absolute; right: 48px; top: 120px; text-align: right; }
  .holder-name {
    font-family: "Michroma", sans-serif; font-size: 19px; letter-spacing: 2px;
    color: var(--teal); text-transform: uppercase;
  }
  .holder-title { font-size: 17px; color: var(--ink); margin-top: 6px; }

  .divider { position: absolute; left: 48px; right: 48px; top: 196px; height: 1px; background: var(--teal); opacity: .6; }

  .address {
    position: absolute; right: 48px; top: 212px;
    font-size: 19px; color: var(--ink); line-height: 1.35; text-align: right;
    display: flex; gap: 10px; align-items: flex-start;
  }

  .contacts { position: absolute; left: 48px; top: 218px; list-style: none; }
  .contacts li {
    display: flex; align-items: center; gap: 10px;
    font-size: 19px; color: var(--ink); line-height: 1.45;
  }
  .icon { width: 18px; height: 18px; flex: none; }
</style>
</head>
<body>

<section class="card card-front" aria-label="Card front">
  <div class="front-brand">
    <div class="brand-row">
      <span class="brand-dot"></span>
      <span class="brand-name">Harbor Shelter Alliance</span>
    </div>
    <div class="brand-rule"></div>
  </div>
</section>

<section class="card card-back" aria-label="Card back">
  <svg class="back-bands" width="700" height="400" viewBox="0 0 700 400" aria-hidden="true">
    <polygon points="0,352 400,330 400,400 0,400" fill="var(--teal-dark)"/>
    <polygon points="408,300 700,270 700,400 408,400" fill="var(--teal)"/>
  </svg>

  <div class="back-brand">
    <span class="brand-dot"></span>
    <span class="brand-name">Harbor Shelter Alliance</span>
  </div>

  <div class="holder">
    <div class="holder-name">Marcus Delaney</div>
    <div class="holder-title">Chairman</div>
  </div>

  <div class="divider"></div>

  <ul class="contacts">
    <li>
      <svg class="icon" viewBox="0 0 18 18"><circle cx="9" cy="9" r="9" fill="var(--teal)"/><path d="M6 5l2 2-1 1a6 6 0 0 0 3 3l1-1 2 2-1.3 1.3C8.5 13 5 9.5 4.7 6.3Z" fill="#fff"/></svg>
      555.014.2290
    </li>
    <li>
      <svg class="icon" viewBox="0 0 18 18"><circle cx="9" cy="9" r="9" fill="var(--teal)"/><circle cx="9" cy="9" r="4.5" fill="none" stroke="#fff" stroke-width="1.2"/><path d="M4.5 9h9M9 4.5c-2 2.5-2 6.5 0 9M9 4.5c2 2.5 2 6.5 0 9" fill="none" stroke="#fff" stroke-width="1"/></svg>
      www.harborshelter.org
    </li>
    <li>
      <svg class="icon" viewBox="0 0 18 18"><circle cx="9" cy="9" r="9" fill="var(--teal)"/><rect x="4.5" y="6" width="9" height="6.5" fill="#fff"/><path d="M4.5 6l4.5 4 4.5-4" fill="none" stroke="var(--teal)" stroke-width="1"/></svg>
      marcus@harborshelter.org
    </li>
  </ul>

  <div class="address">
    <div>P.O Box 270418<br>Riverton, Texas 75900</div>
    <svg class="icon" viewBox="0 0 18 18"><circle cx="9" cy="9" r="9" fill="var(--teal)"/><path d="M9 3.5a3.5 3.5 0 0 1 3.5 3.5c0 2.6-3.5 7-3.5 7S5.5 9.6 5.5 7A3.5 3.5 0 0 1 9 3.5Z" fill="#fff"/><circle cx="9" cy="7" r="1.3" fill="var(--teal)"/></svg>
  </div>
</section>

</body>
</html>
```